BrightPath Dental
Web Presence
BrightPath Dental - Information Technology
Creative Brief
Information Technology
www.brightpathdental-demo.com
Brightpath Dental provides a wide variety of high tech dental solutions at a competitive price. We pride ourselves on the extremely high level and speed of service that we provide to our clientele. We are a local computer company that specializes in bringing our clientele the best dental technology solutions available. By allowing us to correctly integrate the right dental technology solutions, it gives your practice a technological competitive edge, increases production, and significantly enhances your patient’s experience. We provide a full array of computer services for both small and large practices. Our team services PC's and networks, digital x-ray / imaging equipment, we also provide software & hardware sales, service, upgrades, and installations, as well as data storage and backup solutions. We also provide ongoing technical support to keep you comfortable with changing technologies and ensure your practice productivity.
would like CMS designed website for either joomla or wordpress. We need the wording and the design -- we are a Lumoverde Reseller and Installer so please check out their site listed below. our logo is available: http://orders.markcraftstudio-demo.com/contests/business-logo-brightpathdental
left side
http://www.lumoverdedental-demo.com/us_region/index.aspx
http://www.qwbadvisors-demo.com/articles
http://www.orb-sys-demo.com/index.html
Additional Sites that do similar work: http://www.mnzerodental-demo.com/dataprotection.htm http://www.fenwro-demo.com/customer_care.html http://www.glimvo-demo.com/ http://www.mnzerodental-demo.com/dataprotection.htm

```html
<!DOCTYPE html>
<html lang="en">
<head>
<meta charset="utf-8">
<title>BrightPath Dental</title>
<link href="https://fonts.googleapis.com/css2?family=Arimo:wght@400;700&display=swap" rel="stylesheet">
<style>
  :root{
    --page:#f4f5f6;
    --blue:#1e88d2;
    --blue-dark:#0d5fa8;
    --blue-light:#4fb0ee;
    --text:#5d6166;
    --heading:#1878c4;
    --red:#d32a2f;
    --footer-dark:#2b2d30;
    --white:#ffffff;
    --line:#d9dde1;
  }
  *{box-sizing:border-box;margin:0;padding:0}
  html,body{width:1200px;height:1025px;overflow:hidden}
  body{background:var(--page);font-family:"Arimo",Arial,sans-serif;color:var(--text);position:relative}
  .wrap{position:absolute;left:165px;width:870px}

  .brand{position:absolute;left:190px;top:44px;display:flex;align-items:center;gap:12px}
  .brand-dot{width:46px;height:46px;border-radius:50%;background:var(--red)}
  .brand-name{font-size:30px;font-weight:700;color:var(--blue-dark)}

  .social{position:absolute;right:175px;top:54px;display:flex;gap:10px}
  .social span{width:34px;height:34px;border-radius:50%;display:block}
  .s1{background:#3b68b5}.s2{background:#37a8df}.s3{background:#f08a1c}
  .call{position:absolute;right:170px;top:102px;font-size:14px;font-weight:700;color:var(--blue)}

  .nav{top:126px;height:32px;background:linear-gradient(var(--blue-light),var(--blue-dark));border-radius:6px 6px 0 0;display:flex;align-items:center;padding-left:40px}
  .nav a{color:var(--white);font-size:12px;text-decoration:none;margin-right:38px}
  .search{position:absolute;right:20px;top:7px;width:110px;height:18px;background:var(--white);border-radius:9px;font-size:10px;color:#9aa;padding:3px 10px}

  .dropdown{position:absolute;left:258px;top:158px;width:96px;background:rgba(40,44,50,.88);z-index:3;padding:4px 0}
  .dropdown li{list-style:none;font-size:9px;color:#dfe3e6;padding:4px 8px;border-bottom:1px solid rgba(255,255,255,.12)}

  .hero{top:172px;height:352px;border-radius:0 0 6px 6px;overflow:hidden}
  .hero-photo{width:100%;height:100%;background:linear-gradient(120deg,#c5d0d8,#9fb3c2 45%,#e6ecef)}
  .hero-band{position:absolute;left:0;right:0;top:244px;height:52px;background:rgba(40,150,215,.55)}
  .dots{position:absolute;left:42px;top:306px;display:flex;gap:7px}
  .dots i{width:10px;height:10px;border-radius:50%;background:var(--white);opacity:.8}
  .dots i:first-child{background:var(--blue)}
  .next{position:absolute;right:22px;top:251px;display:flex;align-items:center;gap:8px;color:var(--white);font-size:34px}
  .next span{width:30px;height:30px;border-radius:50%;background:var(--red);display:flex;align-items:center;justify-content:center}

  .cards{top:532px;display:flex;justify-content:space-between}
  .card{width:286px}
  .card-head{height:38px;background:linear-gradient(var(--blue-light),var(--blue-dark));color:var(--white);font-size:16px;padding:10px 10px;border-radius:4px 4px 0 0}
  .card-photo{height:118px;border:4px solid var(--white);box-shadow:0 1px 3px rgba(0,0,0,.2)}
  .p1{background:linear-gradient(135deg,#d7e4ee,#8fb4cf)}
  .p2{background:linear-gradient(135deg,#e9d6c8,#b2c6d6)}
  .p3{background:linear-gradient(135deg,#e2e8ee,#9fb0bf)}
  .card h3{font-size:13px;color:var(--heading);margin:22px 0 10px}
  .card p{font-size:10px;line-height:15px}
  .more{margin:22px 0 0 auto;width:62px;display:flex;align-items:center;justify-content:space-between;background:var(--blue-dark);color:var(--white);font-size:10px;border-radius:3px;padding:3px 4px 3px 10px}
  .more span{width:14px;height:14px;border-radius:50%;background:var(--white);color:var(--blue-dark);font-size:9px;text-align:center;line-height:14px}

  .contact{position:absolute;left:0;top:905px;width:1200px;height:78px;background:var(--red);color:var(--white);font-size:10px;text-align:center;padding-top:24px;line-height:18px}
  .bottom{position:absolute;left:0;top:983px;width:1200px;height:42px;background:var(--footer-dark);display:flex;justify-content:center;align-items:center;gap:46px}
  .bottom a{color:#d0d3d6;font-size:11px;text-decoration:none}
</style>
</head>
<body>
  <div class="brand"><span class="brand-dot"></span><span class="brand-name">BrightPath Dental</span></div>
  <div class="social"><span class="s1"></span><span class="s2"></span><span class="s3"></span></div>
  <div class="call">Call Us : 0000 0000 00</div>

  <nav class="wrap nav">
    <a href="#">Home</a><a href="#">About Us</a><a href="#">Dental System</a><a href="#">Our Partners</a><a href="#">Careers</a><a href="#">Contact Us</a>
    <div class="search">Search</div>
  </nav>
  <ul class="dropdown">
    <li>Company Profile</li><li>Our Team</li><li>Installation Services</li><li>Tech Support</li><li>Testimonials</li>
  </ul>

  <section class="wrap hero">
    <div class="hero-photo" role="img" aria-label="Dental team reviewing an x-ray in a clinic"></div>
    <div class="hero-band"></div>
    <div class="dots"><i></i><i></i><i></i><i></i><i></i><i></i></div>
    <div class="next"><span><svg width="14" height="14" viewBox="0 0 14 14"><path d="M4 2l6 5-6 5" fill="none" stroke="#fff" stroke-width="2.5"/></svg></span>Next...</div>
  </section>

  <section class="wrap cards">
    <article class="card">
      <div class="card-head">Dental System</div>
      <div class="card-photo p1" role="img" aria-label="Dental treatment chair and equipment"></div>
      <h3>Orthodontic, OMS and Endodontic Systems</h3>
      <p>At BrightPath we design install and support custom, specialty dental digital network systems. So whether you're a General Dentist, Orthodontist, Oral Surgeon, Endodontist or Periodontist, our technology is customized to suit your patients and to increase staff efficiency. Each system is customized to your practice's needs.</p>
      <div class="more">More <span>&#9656;</span></div>
    </article>
    <article class="card">
      <div class="card-head">Orthodontists</div>
      <div class="card-photo p2" role="img" aria-label="Patient receiving orthodontic care"></div>
      <h3>Orthodontic, OMS and Endodontic Systems</h3>
      <p>At BrightPath we design install and support custom, specialty dental digital network systems. So whether you're a General Dentist, Orthodontist, Oral Surgeon, Endodontist or Periodontist, our technology is customized to suit your patients and to increase staff efficiency. Each system is customized to your practice's needs.</p>
      <div class="more">More <span>&#9656;</span></div>
    </article>
    <article class="card">
      <div class="card-head">Sergeions</div>
      <div class="card-photo p3" role="img" aria-label="Team of dental surgeons"></div>
      <h3>Orthodontic, OMS and Endodontic Systems</h3>
      <p>At BrightPath we design install and support custom, specialty dental digital network systems. So whether you're a General Dentist, Orthodontist, Oral Surgeon, Endodontist or Periodontist, our technology is customized to suit your patients and to increase staff efficiency. Each system is customized to your practice's needs.</p>
      <div class="more">More <span>&#9656;</span></div>
    </article>
  </section>

  <footer class="contact">
    T: (555) 010-2040 &bull; F: (555) 010-2041 &bull; E: info@brightpathdental-demo.com<br>
    Support T: (555) 010-2042 option 1 E: support@brightpathdental-demo.com &nbsp; Sales T: (555) 010-2043 option 2 E: sales@brightpathdental-demo.com
  </footer>
  <nav class="bottom">
    <a href="#">Home</a><a href="#">Specialties</a><a href="#">Dental System</a><a href="#">Our Partners</a><a href="#">Careers</a><a href="#">Contact Us</a>
  </nav>
</body>
</html>
```